new business card

please see the attached business card and logo files, and make the following changes
1-- the little rock clinic address has changed to " suite 927"

2-- lets not " box" the logo

3-- create a " three dimensional " feel of the logo

Target Market(s)

patients and other physicians

Industry/Entity Type

Health Care

Contact Information for Business Card

see the attached files and instructions listed above

Requirements
Must have
• " Veridane Wellness Institute" is the parent organization and therefore has a "center piece" role.
Nice to have
• would like to see a three dimensional feel in the logo
Should not have
• feminine colors -- pink etc.

```html
<!DOCTYPE html>
<html lang="en">
<head>
<meta charset="UTF-8">
<title>Veridane Wellness Institute – Business Card</title>
<link href="https://fonts.googleapis.com/css2?family=Tinos:wght@400;700&display=swap" rel="stylesheet">
<style>
  :root {
    --backdrop: #3a3a3c;
    --card-white: #ffffff;
    --band-dark: #2f3033;
    --ink: #1e1e1e;
    --ink-light: #f4f4f4;
    --accent: #b9bcc2;
    --name-grey: #2a2a2a;
    --rule: #9a9a9a;
  }
  * { box-sizing: border-box; margin: 0; padding: 0; }
  html, body {
    width: 1200px; height: 900px; overflow: hidden;
    background: var(--backdrop);
  }
  .canvas {
    position: relative; width: 1200px; height: 900px;
    display: flex; align-items: center; justify-content: center;
  }
  .business-card {
    position: relative; width: 1000px; height: 570px;
    background: var(--card-white); border-radius: 40px; overflow: hidden;
    font-family: "Tinos", "Times New Roman", serif;
    color: var(--ink);
  }
  .brand {
    position: absolute; left: 60px; top: 44px;
    display: flex; align-items: center; gap: 20px;
  }
  .brand-mark {
    width: 52px; height: 52px; background: var(--band-dark); flex: none;
  }
  .brand-name {
    font-weight: 700; font-size: 46px; line-height: 1; color: var(--band-dark);
    letter-spacing: 0.3px;
  }
  .doctor-name {
    position: absolute; right: 60px; top: 164px;
    font-weight: 700; font-size: 40px; line-height: 1; color: var(--name-grey);
  }
  .contact-band {
    position: absolute; left: 0; right: 0; top: 240px; height: 230px;
    background: var(--band-dark); color: var(--ink-light);
  }
  .office { position: absolute; }
  .office-left { left: 60px; top: 26px; }
  .office-right { left: 560px; top: 70px; }
  .office-title {
    font-weight: 700; font-size: 26px; margin-bottom: 12px;
  }
  .contact-line {
    display: flex; align-items: center; gap: 14px;
    font-size: 19px; font-weight: 700; margin-bottom: 10px;
  }
  .contact-line svg { width: 22px; height: 22px; flex: none; }
  .band-divider { position: absolute; left: 0; top: 0; }
  .website {
    position: absolute; left: 260px; top: 498px;
    font-size: 28px; font-weight: 400; color: var(--ink);
  }
</style>
</head>
<body>
<div class="canvas">
  <div class="business-card">
    <div class="brand">
      <span class="brand-mark"></span>
      <span class="brand-name">Veridane Wellness Institute</span>
    </div>

    <div class="doctor-name">Rohan Ellery M.D.</div>

    <div class="contact-band">
      <svg class="band-divider" width="1000" height="230" aria-hidden="true">
        <line x1="510" y1="30" x2="470" y2="205" stroke="var(--rule)" stroke-width="2"/>
      </svg>

      <div class="office office-left">
        <div class="office-title">Cedar Point Office</div>
        <div class="contact-line">
          <svg viewBox="0 0 24 24"><circle cx="12" cy="12" r="10.5" fill="none" stroke="var(--accent)" stroke-width="1.6"/><path d="M8.5 7c.8-.4 1.3-.2 1.7.5l.8 1.5c.3.6.1 1-.4 1.4l-.5.4c.5 1.2 1.5 2.3 2.7 2.9l.4-.5c.4-.5.9-.6 1.4-.3l1.5.8c.6.4.8.9.4 1.7-.6 1.1-1.8 1.5-3 1-2.8-1.2-4.9-3.4-6-6.2-.4-1.1 0-2.4 1-3.2z" fill="var(--accent)"/></svg>
          501-555-0174
        </div>
        <div class="contact-line">
          <svg viewBox="0 0 24 24"><circle cx="12" cy="12" r="10.5" fill="var(--accent)"/><rect x="8" y="6.5" width="8" height="4" fill="none" stroke="var(--band-dark)" stroke-width="1.3"/><rect x="6.5" y="10" width="11" height="5.5" rx="1" fill="var(--band-dark)"/><rect x="8.5" y="13.5" width="7" height="4" fill="var(--accent)" stroke="var(--band-dark)" stroke-width="1.2"/></svg>
          501-555-0236
        </div>
        <div class="contact-line">
          <svg viewBox="0 0 24 24"><circle cx="12" cy="12" r="10.5" fill="none" stroke="var(--accent)" stroke-width="1.6"/><path d="M12 5.5a4 4 0 0 0-4 4c0 3 4 8 4 8s4-5 4-8a4 4 0 0 0-4-4z" fill="var(--accent)"/><circle cx="12" cy="9.5" r="1.5" fill="var(--band-dark)"/></svg>
          500 S.Harlow Ave.Suite 927 40217
        </div>
      </div>

      <div class="office office-right">
        <div class="office-title">Ashford office</div>
        <div class="contact-line">
          <svg viewBox="0 0 24 24"><circle cx="12" cy="12" r="10.5" fill="none" stroke="var(--accent)" stroke-width="1.6"/><path d="M8.5 7c.8-.4 1.3-.2 1.7.5l.8 1.5c.3.6.1 1-.4 1.4l-.5.4c.5 1.2 1.5 2.3 2.7 2.9l.4-.5c.4-.5.9-.6 1.4-.3l1.5.8c.6.4.8.9.4 1.7-.6 1.1-1.8 1.5-3 1-2.8-1.2-4.9-3.4-6-6.2-.4-1.1 0-2.4 1-3.2z" fill="var(--accent)"/></svg>
          870-555-0188
        </div>
        <div class="contact-line">
          <svg viewBox="0 0 24 24"><circle cx="12" cy="12" r="10.5" fill="var(--accent)"/><rect x="8" y="6.5" width="8" height="4" fill="none" stroke="var(--band-dark)" stroke-width="1.3"/><rect x="6.5" y="10" width="11" height="5.5" rx="1" fill="var(--band-dark)"/><rect x="8.5" y="13.5" width="7" height="4" fill="var(--accent)" stroke="var(--band-dark)" stroke-width="1.2"/></svg>
          870-555-0108
        </div>
        <div class="contact-line">
          <svg viewBox="0 0 24 24"><circle cx="12" cy="12" r="10.5" fill="none" stroke="var(--accent)" stroke-width="1.6"/><path d="M12 5.5a4 4 0 0 0-4 4c0 3 4 8 4 8s4-5 4-8a4 4 0 0 0-4-4z" fill="var(--accent)"/><circle cx="12" cy="9.5" r="1.5" fill="var(--band-dark)"/></svg>
          2865 N. Linden St, 40318
        </div>
      </div>
    </div>

    <div class="website">www.veridanewellness.com</div>
  </div>
</div>
</body>
</html>
```